Steady Crews: Keeping Staff from Drifting Away
Everyday People Guides for the Shopkeeper and Reluctant Personnel Lead
Steady Crews: Keeping Staff from Drifting Away - Books
Creative Brief
title: Everyday People Guides for the Shopkeeper and Reluctant Personnel Lead E-book covers: I'd also like two high-resolution JPG cover images (one front and one back), sized at 5.5" x 8.5" with all elements stopping within .5" of the page edge. A low-resolution version of each image must also be supplied for use in e-book format. These images will include: Front cover: • Image An eye-catching photo/illustration representing the topic of the book (managing costly employee turnover) • Book title Steady Crews: Keeping Staff from Drifting Away • Subtitle with icon Everyday People Guides for the Shopkeeper and Reluctant Personnel Lead, Book 1 • Tagline none • Author name Rosalind Pettigrew, SPHR Back cover: • Image Mugshot of author • Publisher name RTKV Publishing • Author blurb & image (may be inside book) • Barcode Leave space in lower right-hand corner for Bookvane to insert. • Book blurb If you're a small-business owner or entrepreneur thinking, "How in the world do I stop this organization's crazy turnover?" this e-book is for you. Steady Crews: Keeping Staff from Drifting Away by certified Human Resources consultant Rosalind Pettigrew provides simple tools for those thrown into the role of "accidental HR manager." Compiled as book one in Pettigrew's series, Everyday People Guides for the Shopkeeper and Reluctant Personnel Lead, it delivers quick access to critical, yet simple, techniques and processes to help you manage HR issues like recruitment/hiring, performance, and more. Filled with explanations and advice, worksheets and handy calculators, you'll find a solid foundation of information to help you manage your organization's HR issues... without the learning curve.
Books
Corporate executives in small businesses and entrepreneurs tasked with the role of managing Human Resources unexpectedly.
Book one cover art: • Book series icon • 2 high-resolution JPG files (1 front cover, 1 back cover) • 5.5" x 8.5" final size, with a .5" margin at all page edges • 2 low-res JPG files of the same front- and back-cover art for use in e-book format • Book title must be large enough to read in thumbnail size (like book thumbnails viewed on Bookvane) • Designer will need to procure: o Author mug shot (if not inside book) o Final book blurb for back cover o Book formatting specs from PrintHollow.com

```html
<!DOCTYPE html>
<html lang="en">
<head>
<meta charset="utf-8">
<title>Steady Crews: Keeping Staff from Drifting Away — Cover Spread</title>
<link rel="stylesheet" href="https://fonts.googleapis.com/css2?family=Arimo:wght@400;700&display=swap">
<style>
  :root {
    --page: #ffffff;
    --backdrop: #f4f4f4;
    --ink: #111111;
    --ink-soft: #555555;
    --spine-band: #6e6e6e;
    --spine-band-text: #ffffff;
    --edge: #d8d8d8;
    --photo-light: #eceeef;
    --photo-dark: #4a4f56;
  }
  * { box-sizing: border-box; margin: 0; padding: 0; }
  html, body {
    width: 1200px; height: 670px; overflow: hidden;
    background: var(--backdrop);
    font-family: "Arimo", Arial, sans-serif;
    color: var(--ink);
  }
  .spread {
    position: absolute; left: 213px; top: 55px;
    width: 774px; height: 560px;
    display: flex;
    background: var(--page);
    box-shadow: 0 2px 10px rgba(0,0,0,0.12);
  }
  .back-cover, .front-cover {
    position: relative; width: 362px; height: 560px;
    border: 1px solid var(--edge);
  }
  .spine {
    position: relative; width: 50px; height: 560px;
    border-top: 1px solid var(--edge); border-bottom: 1px solid var(--edge);
    background: var(--page);
  }
  .back-blurb {
    position: absolute; left: 30px; top: 36px; width: 300px;
    font-size: 9.5px; line-height: 1.35; color: var(--ink);
  }
  .publisher {
    position: absolute; left: 30px; bottom: 40px;
    font-size: 13px; color: var(--ink);
  }
  .spine-author-band {
    position: absolute; left: 0; top: 0; width: 100%; height: 170px;
    background: var(--spine-band);
    display: flex; align-items: center; justify-content: center;
  }
  .spine-author {
    writing-mode: vertical-rl;
    font-size: 13px; color: var(--spine-band-text); letter-spacing: 0.5px;
  }
  .spine-title {
    position: absolute; left: 0; top: 190px; width: 100%; height: 350px;
    display: flex; justify-content: center;
    writing-mode: vertical-rl;
    font-size: 14px; font-weight: 700; white-space: nowrap;
  }
  .front-author {
    position: absolute; left: 0; top: 44px; width: 100%;
    text-align: center; font-size: 15px; color: var(--ink-soft);
  }
  .cover-photo {
    position: absolute; left: 70px; top: 96px; width: 210px; height: 440px;
  }
  .front-title {
    position: absolute; left: 26px; top: 138px; width: 320px;
    font-size: 27px; font-weight: 700; line-height: 1.1; color: var(--ink);
  }
  .front-subtitle {
    position: absolute; left: 26px; top: 232px; width: 250px;
    font-size: 12.5px; font-weight: 700; line-height: 1.3; color: var(--ink);
  }
</style>
</head>
<body>
  <main class="spread">
    <section class="back-cover">
      <p class="back-blurb">If you're a small-business owner or entrepreneur thinking, "How in the world do I stop this organization's crazy turnover?" this e-book is for you. Steady Crews: Keeping Staff from Drifting Away by certified Human Resources consultant Rosalind Pettigrew provides simple tools for those thrown into the role of "accidental HR manager."<br><br>Compiled as book one in Pettigrew's series, Everyday People Guides for the Shopkeeper and Reluctant Personnel Lead, it delivers quick access to critical, yet simple, techniques and processes to help you manage HR issues like recruitment/hiring, performance, and more. Filled with explanations and advice, worksheets and handy calculators, you'll find a solid foundation of information to help you manage your organization's HR issues... without the learning curve.</p>
      <p class="publisher">RTKV Publishing</p>
    </section>

    <section class="spine">
      <div class="spine-author-band"><span class="spine-author">Rosalind Pettigrew, SPHR</span></div>
      <div class="spine-title">Steady Crews: Keeping Staff from Drifting Away</div>
    </section>

    <section class="front-cover">
      <p class="front-author">Rosalind Pettigrew, SPHR</p>
      <svg class="cover-photo" role="img" aria-label="Photo of a businessman in a dark suit walking away with a briefcase" viewBox="0 0 210 440" preserveAspectRatio="none">
        <defs>
          <linearGradient id="photoTone" x1="0" y1="0" x2="0" y2="1">
            <stop offset="0" stop-color="var(--photo-light)"/>
            <stop offset="0.35" stop-color="var(--photo-dark)"/>
            <stop offset="1" stop-color="var(--photo-dark)"/>
          </linearGradient>
        </defs>
        <rect width="210" height="440" fill="url(#photoTone)" opacity="0.85"/>
      </svg>
      <h1 class="front-title">Steady Crews: Keeping Staff from Drifting Away</h1>
      <p class="front-subtitle">Everyday People Guides for the Shopkeeper and Reluctant Personnel Lead<br>Book 1</p>
    </section>
  </main>
</body>
</html>
```